Buchcover-Design für Coaching-Buch
Zielgruppe
22 Coaches (m/w/d) haben zusammen ein Buch geschrieben - mit ihren besten Tipps, Mut machenden Geschichten und Inspirationen. Herausgekommen ist 'Die stille Begleiterin fürs Kopfkissen - 22 Schatztruhen öffnen ihre Schubladen'. Zielgruppe sind vorwiegend Frauen, häufig mit spirituellem Hintergrund oder an Selbstentwicklung interessiert, sowie Menschen, die sich ermutigen lassen möchten und Menschen, die inspirierende Texte und Geschichten mögen. Die Themen sind ganz unterschiedlich, von Selbstliebe über die Wirkung von Farben, vom Überwinden von Krisen und Angst, Umgang mit Emotionen etc. pp. - ein ganzer Blumenstrauß an Themen.
Aufgabenstellung
Der Titel 'Die stille Begleiterin fürs Kopfkissen' kam auf, weil wir die Vorstellung hatten, dass in dem Buch vielleicht abends im Bett gelesen wird und man dann ruhig schlafen kann.
Warum Füllhörner? Nun, jeder Coach hat viel zu geben. Zu jedem Text wird es ein Geschenk geben, das die Autor*innen online zur Verfügung stellen. Dies sind PDFs mit Tipps, Meditationen oder sogar eine kurze Gratis-Session. Es braucht also etwas auf dem Cover, das darauf hindeutet, vielleicht eine Plakette oder etwas Ähnliches, das 'Mit 22 Geschenken' besagt. Im Buchsatz wird dies durch einen Link (E-Book) und durch einen QR-Code (Print) umgesetzt.

```html
<!DOCTYPE html>
<html lang="de">
<head>
<meta charset="utf-8">
<title>Die stille Begleiterin fürs Kopfkissen – Buchcover</title>
<link rel="stylesheet" href="https://fonts.googleapis.com/css2?family=Lexend:wght@400&family=Lato:wght@400&display=swap">
<style>
  :root {
    --page-bg: #e4e4e2;
    --cover-bg: #ffffff;
    --plum: #8c3d78;
    --badge-text: #ffffff;
    --art-pink: #e0467f;
    --art-magenta: #c24a9c;
    --art-violet: #8a5fb8;
    --art-blue: #4f78c8;
  }
  html, body {
    margin: 0;
    padding: 0;
    width: 1169px;
    height: 1200px;
    overflow: hidden;
    background: var(--page-bg);
  }
  .book-cover {
    position: absolute;
    left: 196px;
    top: 30px;
    width: 777px;
    height: 1140px;
    background: var(--cover-bg);
    overflow: hidden;
  }
  .cover-art {
    position: absolute;
    left: 0;
    top: 0;
    width: 560px;
    height: 1140px;
  }
  .cover-title {
    position: absolute;
    right: 63px;
    top: 100px;
    margin: 0;
    text-align: right;
    font-family: "Lexend", sans-serif;
    font-weight: 400;
    font-size: 58px;
    line-height: 67px;
    color: var(--plum);
    letter-spacing: 0.5px;
  }
  .cover-subtitle {
    position: absolute;
    right: 63px;
    top: 552px;
    margin: 0;
    text-align: right;
    font-family: "Lato", sans-serif;
    font-size: 19px;
    line-height: 26px;
    letter-spacing: 0.6px;
    color: var(--plum);
    text-transform: uppercase;
  }
  .gift-badge {
    position: absolute;
    left: 527px;
    top: 962px;
    width: 262px;
    height: 42px;
    background: var(--plum);
    color: var(--badge-text);
    font-family: "Lato", sans-serif;
    font-size: 18px;
    letter-spacing: 0.6px;
    line-height: 42px;
    padding-left: 18px;
    box-sizing: border-box;
    transform: rotate(-4deg);
    transform-origin: left center;
    text-transform: uppercase;
  }
</style>
</head>
<body>
  <main class="book-cover">
    <svg class="cover-art" role="img" aria-label="Doppelbelichtung: Profil einer nachdenklichen Frau mit Hand am Kinn, überlagert von pinken, violetten und blauen Pinselstrichen" viewBox="0 0 560 1140" preserveAspectRatio="none">
      <defs>
        <linearGradient id="art-colour" x1="0" y1="0" x2="0.4" y2="1">
          <stop offset="0" stop-color="var(--art-pink)"/>
          <stop offset="0.35" stop-color="var(--art-magenta)"/>
          <stop offset="0.7" stop-color="var(--art-violet)"/>
          <stop offset="1" stop-color="var(--art-blue)"/>
        </linearGradient>
        <linearGradient id="art-fade" x1="0" y1="0" x2="1" y2="0">
          <stop offset="0" stop-color="#fff" stop-opacity="1"/>
          <stop offset="0.6" stop-color="#fff" stop-opacity="0.85"/>
          <stop offset="1" stop-color="#fff" stop-opacity="0"/>
        </linearGradient>
        <mask id="art-mask">
          <rect width="560" height="1140" fill="url(#art-fade)"/>
        </mask>
      </defs>
      <path d="M0 0 H340 C420 120 440 320 380 480 C340 600 420 760 400 900 C390 1010 360 1100 340 1140 H0 Z" fill="url(#art-colour)" mask="url(#art-mask)" opacity="0.85"/>
    </svg>

    <h1 class="cover-title">Die<br>stille<br>Beglei-<br>terin fürs<br>Kopf-<br>kissen</h1>

    <p class="cover-subtitle">22 Schatztruhen<br>öffnen ihre<br>Schubladen.</p>

    <div class="gift-badge">Mit 22 Geschenken</div>
  </main>
</body>
</html>
```